Medical Device Packaging Project 4 of 5

We are a medical device startup company needing packaging for a total of 5 device brands. This is posting 4 of 5 and the device name is "Velotin"

Velotin is an intraocular lens for use in cataract surgery. The target market is Chinese ophthalmologists. The box should be sophisticated and upmarket.

The company name is Cendra Optics, I have included the logo in the uploaded files section. You should include the logo on the box.

I have uploaded a sample lens boxes from other companies that demonstrate the information needed to be contained on the box in terms of address, warnings, symbols, etc.

I have also uploaded the blank dieline of the boxes

You are welcome and encouraged to also submit to projects 1, 2, 3, and 5 as well. The same rules and expectations apply.

Industry/Entity Type

It Company

Requirements
Should not have
• Should not have any images of an eye or any bionic/futuristic feel to the design
• Note that the halvisen box is for text reference only. You may use the lens image but the futuristic/bionic look is NOT what we are going for with this brand. It should be traditional upmarket medical device artwork.

```html
<!DOCTYPE html>
<html lang="en">
<head>
<meta charset="utf-8">
<title>Velotin – Intraocular Lens Carton Dieline</title>
<link rel="stylesheet" href="https://fonts.googleapis.com/css2?family=Exo+2:wght@400;500&family=Roboto+Condensed:wght@400&family=Noto+Sans+SC:wght@400&display=swap">
<style>
  :root {
    --paper: #ffffff;
    --flap-blue: #1b4c89;
    --flap-edge: #15407a;
    --panel-light: #a9c6e0;
    --panel-mid: #5f92c4;
    --panel-deep: #2a62a0;
    --grid-tone: #3f7ac0;
    --lens-light: #e6f3f8;
    --lens-mid: #9cc3d6;
    --ink-white: #ffffff;
    --ink-dim: #d7e6f4;
    --dim-ink: #333333;
  }
  html, body {
    margin: 0;
    padding: 0;
    width: 800px;
    height: 1200px;
    overflow: hidden;
    background: var(--paper);
  }
  .dieline { display: block; width: 800px; height: 1200px; }
  .dimension { font-family: "Times New Roman", serif; font-size: 13px; fill: var(--dim-ink); }
  .brand-name { font-family: "Exo 2", sans-serif; font-weight: 500; fill: var(--ink-white); letter-spacing: 1.5px; }
  .product-name { font-family: "Exo 2", sans-serif; font-weight: 500; fill: var(--ink-white); letter-spacing: 2px; }
  .tagline { font-family: "Exo 2", sans-serif; font-weight: 400; fill: var(--ink-white); }
  .spec-line { font-family: "Exo 2", sans-serif; font-weight: 400; fill: var(--ink-white); font-size: 9px; letter-spacing: 0.3px; }
  .address { font-family: "Exo 2", sans-serif; font-size: 11px; fill: var(--ink-white); letter-spacing: 0.5px; }
  .notice { font-family: "Roboto Condensed", sans-serif; font-size: 8.2px; fill: var(--ink-dim); }
  .notice-cn { font-family: "Noto Sans SC", sans-serif; font-size: 9px; fill: var(--ink-dim); letter-spacing: 2px; }
  .notice-rule { stroke: var(--ink-dim); stroke-width: 1; }
  .symbol { fill: none; stroke: var(--ink-white); stroke-width: 1.2; }
  .symbol-text { font-family: "Exo 2", sans-serif; font-size: 8px; fill: var(--ink-white); }
  .flap { fill: var(--flap-blue); }
  .grid-field { fill: var(--grid-tone); opacity: 0.55; }
</style>
</head>
<body>
<svg class="dieline" viewBox="100 430 840 1260" preserveAspectRatio="xMidYMid meet" xmlns="http://www.w3.org/2000/svg">
  <defs>
    <radialGradient id="panel-front" cx="55%" cy="40%" r="75%">
      <stop offset="0" stop-color="var(--panel-light)"/>
      <stop offset="0.55" stop-color="var(--panel-mid)"/>
      <stop offset="1" stop-color="var(--panel-deep)"/>
    </radialGradient>
    <linearGradient id="panel-band" x1="0" y1="0" x2="0" y2="1">
      <stop offset="0" stop-color="var(--panel-deep)"/>
      <stop offset="0.5" stop-color="var(--panel-mid)"/>
      <stop offset="1" stop-color="var(--panel-deep)"/>
    </linearGradient>
    <linearGradient id="panel-side" x1="0" y1="0" x2="1" y2="0">
      <stop offset="0" stop-color="var(--panel-deep)"/>
      <stop offset="0.5" stop-color="var(--panel-mid)"/>
      <stop offset="1" stop-color="var(--panel-deep)"/>
    </linearGradient>
    <radialGradient id="lens-tone" cx="50%" cy="45%" r="55%">
      <stop offset="0" stop-color="var(--lens-light)"/>
      <stop offset="0.7" stop-color="var(--lens-mid)" stop-opacity="0.8"/>
      <stop offset="1" stop-color="var(--lens-mid)" stop-opacity="0"/>
    </radialGradient>
  </defs>

  <!-- dimensions -->
  <g class="dimensions">
    <text class="dimension" x="262" y="496" text-anchor="middle">35mm</text>
    <text class="dimension" x="513" y="502" text-anchor="middle">128mm</text>
    <text class="dimension" x="798" y="496" text-anchor="middle">35mm</text>
    <text class="dimension" x="157" y="622" text-anchor="middle">18mm</text>
    <text class="dimension" x="900" y="622" text-anchor="middle">18mm</text>
    <text class="dimension" transform="translate(114 800) rotate(-90)" text-anchor="middle">90mm</text>
    <text class="dimension" transform="translate(187 576) rotate(-90)" text-anchor="middle">35mm</text>
    <text class="dimension" transform="translate(187 1022) rotate(-90)" text-anchor="middle">35mm</text>
    <text class="dimension" transform="translate(277 1276) rotate(-90)" text-anchor="middle">90mm</text>
    <text class="dimension" transform="translate(280 1460) rotate(-90)" text-anchor="middle">12mm</text>
  </g>

  <!-- dust flaps -->
  <g class="dust-flaps">
    <polygon class="flap" points="205,537 308,513 308,640 300,628 205,628"/>
    <polygon class="flap" points="748,513 850,537 850,628 756,628 748,640"/>
    <polygon class="flap" points="205,987 300,987 308,972 308,1100 205,1080"/>
    <polygon class="flap" points="748,972 756,987 850,987 850,1080 748,1100"/>
  </g>

  <!-- top tuck panel -->
  <g class="panel-top-tuck">
    <rect x="308" y="513" width="440" height="127" fill="url(#panel-band)"/>
    <rect class="grid-field" x="322" y="530" width="168" height="92" role="img" aria-label="Field of small blue squares"/>
    <g transform="rotate(180 632 575)">
      <text class="address" x="550" y="556">CENDRA OPTICS LIMITED</text>
      <text class="address" x="550" y="571">HONG KONG</text>
      <text class="address" x="550" y="586">www.cendraoptics.com</text>
    </g>
  </g>

  <!-- glue flap + left side -->
  <g class="panel-left-side">
    <path class="flap" d="M140,640 H190 V972 H140 Q125,972 125,957 V655 Q125,640 140,640 Z"/>
    <rect x="188" y="640" width="120" height="332" fill="url(#panel-side)"/>
    <rect class="grid-field" x="215" y="650" width="86" height="180" role="img" aria-label="Field of small blue squares"/>
    <text class="brand-name" font-size="15" transform="translate(250 900) rotate(90)" text-anchor="middle">CENDRA OPTICS</text>
  </g>

  <!-- front panel -->
  <g class="panel-front">
    <rect x="308" y="640" width="440" height="332" fill="url(#panel-front)"/>
    <ellipse cx="520" cy="790" rx="120" ry="95" fill="url(#lens-tone)" role="img" aria-label="Intraocular lens with haptics and light beams"/>
    <text class="brand-name" x="663" y="724" font-size="20" text-anchor="middle">CENDRA OPTICS</text>
    <text class="spec-line" x="663" y="784" text-anchor="middle">HYDROPHOBIC ACRYLIC</text>
    <text class="spec-line" x="663" y="794" text-anchor="middle">INTRAOCULAR LENS</text>
    <rect class="grid-field" x="315" y="875" width="166" height="92" role="img" aria-label="Field of small blue squares"/>
    <text class="product-name" x="330" y="921" font-size="23">VELOTIN</text>
    <text class="tagline" x="330" y="937" font-size="11">WITH 360° SQUARE EDGE</text>
  </g>

  <!-- right side + end flap -->
  <g class="panel-right-side">
    <rect x="748" y="640" width="120" height="332" fill="url(#panel-side)"/>
    <path class="flap" d="M866,640 H915 Q930,640 930,655 V957 Q930,972 915,972 H866 Z"/>
    <text class="brand-name" font-size="15" transform="translate(805 715) rotate(-90)" text-anchor="middle">CENDRA OPTICS</text>
    <rect class="grid-field" x="755" y="785" width="86" height="180" role="img" aria-label="Field of small blue squares"/>
    <g class="side-symbols">
      <circle class="symbol" cx="855" cy="829" r="5"/>
      <circle class="symbol" cx="855" cy="855" r="5"/>
      <circle class="symbol" cx="855" cy="880" r="5"/>
      <text class="symbol-text" x="855" y="883" text-anchor="middle" font-size="7">2</text>
      <polygon class="symbol" points="855,900 850,911 860,911"/>
      <rect class="symbol" x="850" y="925" width="10" height="38"/>
    </g>
  </g>

  <!-- bottom band panel -->
  <g class="panel-bottom-band">
    <rect x="308" y="972" width="440" height="128" fill="url(#panel-band)"/>
    <text class="brand-name" x="415" y="1044" font-size="17" text-anchor="middle">CENDRA OPTICS</text>
    <rect class="grid-field" x="565" y="993" width="167" height="90" role="img" aria-label="Field of small blue squares"/>
    <text class="product-name" x="590" y="1029" font-size="21">VELOTIN</text>
    <text class="spec-line" x="590" y="1044">HYDROPHOBIC ACRYLIC</text>
    <text class="spec-line" x="590" y="1054">INTRAOCULAR LENS</text>
    <text class="spec-line" x="590" y="1064">WITH 360° SQUARE EDGE</text>
  </g>

  <!-- back panel -->
  <g class="panel-back">
    <rect x="308" y="1100" width="440" height="335" fill="url(#panel-front)"/>
    <ellipse cx="405" cy="1225" rx="85" ry="100" fill="url(#lens-tone)" role="img" aria-label="Intraocular lens with curved haptics"/>
    <rect class="grid-field" x="315" y="1335" width="166" height="92" role="img" aria-label="Field of small blue squares"/>
    <text class="product-name" x="330" y="1382" font-size="23">VELOTIN</text>
    <text class="tagline" x="330" y="1398" font-size="11">WITH 360° SQUARE EDGE</text>

    <g class="notices">
      <line class="notice-rule" x1="543" y1="1117" x2="543" y2="1150"/>
      <text class="notice" x="550" y="1125">CONTAINS ONE STERILE INTRAOCULAR LENS</text>
      <text class="notice" x="550" y="1136">DO NOT USE IF THE PACKAGE IS DAMAGED</text>
      <text class="notice" x="550" y="1147">DO NOT RESTERILIZE</text>

      <line class="notice-rule" x1="543" y1="1160" x2="543" y2="1196"/>
      <text class="notice-cn" x="550" y="1170">内含无菌的眼内透镜一个</text>
      <text class="notice-cn" x="550" y="1182">如果包装被损坏，请勿使用</text>
      <text class="notice-cn" x="550" y="1194">请勿重新消毒</text>

      <line class="notice-rule" x1="543" y1="1207" x2="543" y2="1240"/>
      <text class="notice" x="550" y="1215">CONTIENT UNE STÉRILE LENTILLE INTRAOCULAIRE</text>
      <text class="notice" x="550" y="1226">NE PAS UTILISER SI LE FORFAIT EST ENDOMMAGÉ</text>
      <text class="notice" x="550" y="1237">NE PAS RESTÉRILISER</text>

      <line class="notice-rule" x1="543" y1="1252" x2="543" y2="1285"/>
      <text class="notice" x="550" y="1260">CONTIENE UNO STERILE LENTE INTRAOCULARE</text>
      <text class="notice" x="550" y="1271">NON USARE SE IL PACCHETTO È DANNEGGIATO</text>
      <text class="notice" x="550" y="1282">NON RISTERILIZZARE</text>

      <line class="notice-rule" x1="543" y1="1298" x2="543" y2="1331"/>
      <text class="notice" x="550" y="1306">ENTHÄLT EINE STERILISCHE INTRAOKULARE LINSE</text>
      <text class="notice" x="550" y="1317">NICHT VERWENDEN, WENN DAS PAKET SCHÄDIGT WIRD</text>
      <text class="notice" x="550" y="1328">NICHT RESERVIEREN</text>

      <line class="notice-rule" x1="543" y1="1343" x2="543" y2="1376"/>
      <text class="notice" x="550" y="1351">BEVAT ÉÉN STERIELE INTRAOCULAIRE LENS</text>
      <text class="notice" x="550" y="1362">NIET GEBRUIKEN ALS DE VERPAKKING BESCHADIGD IS</text>
      <text class="notice" x="550" y="1373">NIET OPNIEUW STERILISEREN</text>
    </g>

    <g class="symbols">
      <rect class="symbol" x="535" y="1400" width="37" height="20"/>
      <rect class="symbol" x="572" y="1400" width="18" height="20"/>
      <text class="symbol-text" x="553" y="1413" text-anchor="middle">STERILE</text>
      <text class="symbol-text" x="581" y="1413" text-anchor="middle">EO</text>
      <polygon class="symbol" points="614,1398 601,1421 627,1421"/>
      <line class="symbol" x1="614" y1="1405" x2="614" y2="1414"/>
      <circle class="symbol" cx="648" cy="1410" r="11"/>
      <text class="symbol-text" x="648" y="1414" text-anchor="middle" font-size="11">2</text>
      <line class="symbol" x1="640" y1="1402" x2="656" y2="1418"/>
      <circle class="symbol" cx="678" cy="1410" r="11"/>
      <line class="symbol" x1="670" y1="1402" x2="686" y2="1418"/>
      <circle class="symbol" cx="710" cy="1410" r="11"/>
      <rect class="symbol" x="704" y="1405" width="12" height="9"/>
      <line class="symbol" x1="702" y1="1402" x2="718" y2="1418"/>
    </g>
  </g>

  <!-- bottom tuck -->
  <rect class="flap" x="308" y="1435" width="440" height="43"/>
</svg>
</body>
</html>
```